standardize print collateral

we need help standardizing all print collateral and website. top priorities:

1. standardized case studies template
2. standardized marketing slicks template
3. standardized powerpoint template
Updates

Project Deadline Extended
Reason: We are extending the project to allow current design submissions to be tweaked while providing the opportunity for new designs to be submitted. We will need all 3 collateral designs submitted to make a final decision. Please note, these 3 designs should all look different, needless to say they should all compliment eachother. As for some direction, the powerpoint main color should not be yellow since yellow does not show up the same shade on any screen. The case study and marketing slicks will be printed and often sit next to our competitors marketing material - think high end product, technology, revolutionary, edgy, professional. The designs should compliment eachother and feel like the Brightfen Metrics brand (which you are determining) and should stand out professionally. We are open to introducing new colors into our brand, the only thing that must remain the same is our logo. Have fun, make it edgy, and keep it professional. Looking forward to seeing what you submit!

Target Market(s)

Property Casualty Insurance Companies: Executive level wording with actuarial credibility

Industry/Entity Type

Marketing

Requirements
Must have
• professional layout for existing collateral and 2-page marketing slicks. style guide/colors can be transferred to powerpoint. logo must stay; everything else (i.e. color, font, layout/structure etc.) is flexible. The three components should not looks the same, they should only compliment eachother.
Nice to have
• we are revolutionizing a conservative industry, so adequate level of edgy/advanced technology/impactful feel to layout
Should not have
• no need to stay within color constraints of yellow, but need to appropriately work well with the eagle head logo

```html
<!DOCTYPE html>
<html lang="en">
<head>
<meta charset="utf-8">
<title>Brightfen Metrics – Portfolio Analytics</title>
<link href="https://fonts.googleapis.com/css2?family=Carlito:wght@400;700&family=Arimo:wght@400;700&display=swap" rel="stylesheet">
<style>
  :root{
    --gold:#f0b41c;
    --gold-deep:#c98f0a;
    --ink:#111111;
    --text:#1c1c1c;
    --muted:#595959;
    --rule:#c8c8c8;
    --bar:#4a7ebb;
    --grid:#d9d9d9;
    --paper:#ffffff;
  }
  html,body{margin:0;padding:0;overflow:hidden;background:var(--paper);}
  .sheet{position:relative;width:847px;height:1200px;overflow:hidden;background:var(--paper);font-family:'Carlito',Calibri,sans-serif;color:var(--text);}
  .header-band{position:absolute;left:0;top:0;width:590px;height:181px;background:linear-gradient(90deg,var(--gold) 0%,var(--gold) 55%,var(--gold-deep) 80%,var(--ink) 100%);}
  .headline{position:absolute;left:0;width:847px;top:254px;text-align:center;font-size:20px;line-height:26px;margin:0;font-weight:400;}
  .feature-panel{position:absolute;left:73px;top:335px;width:703px;height:633px;border:1px solid var(--rule);box-sizing:border-box;}
  .divider-v{position:absolute;left:352px;top:0;width:1px;height:325px;background:var(--rule);}
  .divider-h{position:absolute;left:0;top:325px;width:701px;height:1px;background:var(--rule);}
  .chart{position:absolute;font-family:'Carlito',Calibri,sans-serif;}
  .chart text{fill:#333;}
  .chart .title{font-weight:700;font-size:15px;fill:var(--text);}
  .chart .tick{font-size:6.5px;}
  .chart .axis-title{font-size:6.5px;font-weight:700;}
  .caption{position:absolute;font-family:'Arimo',Arial,sans-serif;font-size:16.5px;line-height:17.5px;color:var(--muted);margin:0;text-align:justify;}
  .caption-wide{position:absolute;left:46px;width:620px;top:352px;font-family:'Arimo',Arial,sans-serif;font-size:16.5px;line-height:19px;color:var(--muted);margin:0;}
  .closing{position:absolute;left:0;width:847px;top:990px;text-align:center;font-size:17px;line-height:22px;margin:0;}
  .about{position:absolute;left:82px;width:700px;top:1054px;font-size:15.5px;line-height:19px;letter-spacing:0.25px;color:var(--muted);margin:0;}
  .footer-rule{position:absolute;left:30px;width:795px;top:1104px;height:1px;background:var(--gold);}
  .footer{position:absolute;left:0;width:847px;top:1113px;text-align:center;font-size:13.5px;line-height:17px;margin:0;}
  .footer .company{font-size:15px;display:block;margin-bottom:1px;}
</style>
</head>
<body>
<div class="sheet">
  <div class="header-band" role="img" aria-label="Brand header graphic in gold and black"></div>

  <h1 class="headline">Ridgeline detects, measures and presents actionable options to correct the<br>effects of adverse selection within any P&amp;C portfolio.</h1>

  <section class="feature-panel">
    <div class="divider-v"></div>
    <div class="divider-h"></div>

    <svg class="chart" style="left:17px;top:18px" width="320" height="200" viewBox="0 0 320 200">
      <text class="title" x="175" y="16" text-anchor="middle">Underwriting Score</text>
      <g stroke="var(--grid)" stroke-width="0.8">
        <line x1="50" x2="300" y1="32" y2="32"/><line x1="50" x2="300" y1="47.6" y2="47.6"/>
        <line x1="50" x2="300" y1="63.3" y2="63.3"/><line x1="50" x2="300" y1="78.9" y2="78.9"/>
        <line x1="50" x2="300" y1="94.5" y2="94.5"/><line x1="50" x2="300" y1="110.1" y2="110.1"/>
        <line x1="50" x2="300" y1="125.8" y2="125.8"/><line x1="50" x2="300" y1="141.4" y2="141.4"/>
      </g>
      <line x1="50" x2="300" y1="157" y2="157" stroke="#888" stroke-width="0.8"/>
      <line x1="50" x2="50" y1="32" y2="157" stroke="#888" stroke-width="0.8"/>
      <g class="tick" text-anchor="end">
        <text x="46" y="34">80%</text><text x="46" y="50">70%</text><text x="46" y="65">60%</text>
        <text x="46" y="81">50%</text><text x="46" y="97">40%</text><text x="46" y="112">30%</text>
        <text x="46" y="128">20%</text><text x="46" y="143">10%</text><text x="46" y="159">0%</text>
      </g>
      <g fill="var(--bar)">
        <rect x="59" y="49.2" width="24" height="107.8"/>
        <rect x="100.7" y="80.4" width="24" height="76.6"/>
        <rect x="142.4" y="108.6" width="24" height="48.4"/>
        <rect x="184.1" y="113.3" width="24" height="43.7"/>
        <rect x="225.8" y="125.8" width="24" height="31.2"/>
        <rect x="267.5" y="128.9" width="24" height="28.1"/>
      </g>
      <g class="tick" text-anchor="middle">
        <text x="71" y="167">0-98</text><text x="112.7" y="167">99 - 249</text>
        <text x="154.4" y="167">250 - 499</text><text x="196.1" y="167">500 - 749</text>
        <text x="237.8" y="167">750 - 899</text><text x="279.5" y="167">900 - 1000</text>
      </g>
      <text class="axis-title" x="175" y="178" text-anchor="middle">Score Tier</text>
      <text class="axis-title" transform="translate(20,95) rotate(-90)" text-anchor="middle">Loss Ratio</text>
    </svg>
    <p class="caption" style="left:43px;top:236px;width:268px;">Discover the pricing imbalances within the portfolio. These imbalances are the main driver of the adverse selection</p>

    <svg class="chart" style="left:375px;top:18px" width="310" height="200" viewBox="0 0 310 200">
      <text class="title" x="165" y="16" text-anchor="middle">Trend and Loss Ratio</text>
      <g stroke="var(--grid)" stroke-width="0.8">
        <line x1="40" x2="290" y1="35" y2="35"/><line x1="40" x2="290" y1="55" y2="55"/>
        <line x1="40" x2="290" y1="75" y2="75"/><line x1="40" x2="290" y1="95" y2="95"/>
        <line x1="40" x2="290" y1="115" y2="115"/><line x1="40" x2="290" y1="135" y2="135"/>
      </g>
      <line x1="40" x2="290" y1="155" y2="155" stroke="#888" stroke-width="0.8"/>
      <line x1="40" x2="40" y1="35" y2="155" stroke="#888" stroke-width="0.8"/>
      <line x1="140" x2="140" y1="35" y2="155" stroke="#888" stroke-width="0.8"/>
      <g class="tick" text-anchor="end">
        <text x="36" y="37">60%</text><text x="36" y="57">50%</text><text x="36" y="77">40%</text>
        <text x="36" y="97">30%</text><text x="36" y="117">20%</text><text x="36" y="137">10%</text><text x="36" y="157">0%</text>
      </g>
      <g class="tick" text-anchor="middle">
        <text x="40" y="165">-40%</text><text x="90" y="165">-20%</text><text x="140" y="165">0%</text>
        <text x="190" y="165">20%</text><text x="240" y="165">40%</text><text x="290" y="165">60%</text>
      </g>
      <text class="axis-title" x="165" y="175" text-anchor="middle">Growth/Decline</text>
      <text class="axis-title" transform="translate(14,95) rotate(-90)" text-anchor="middle">Loss Ratio</text>
      <defs>
        <radialGradient id="bubble" cx="40%" cy="35%" r="65%">
          <stop offset="0" stop-color="#e8eef8"/><stop offset="1" stop-color="#9db6dc"/>
        </radialGradient>
      </defs>
      <g fill="url(#bubble)" stroke="#b6c8e6" stroke-width="0.6">
        <circle cx="235" cy="53" r="16"/>
        <circle cx="112.5" cy="69" r="15"/>
        <circle cx="102.5" cy="93" r="17"/>
        <circle cx="77.5" cy="111" r="16"/>
      </g>
      <line x1="40" x2="290" y1="75" y2="75" stroke="var(--bar)" stroke-width="1.6"/>
      <g class="tick" text-anchor="middle">
        <text x="235" y="56">1</text><text x="112.5" y="72">3</text>
        <text x="102.5" y="96">4</text><text x="77.5" y="114">2</text>
        <text x="282" y="72">40%</text>
      </g>
    </svg>
    <p class="caption" style="left:395px;top:236px;width:272px;">Show trends within the portfolio in real time covering premium adequacy and the quality of all business being written.</p>

    <p class="caption-wide">Report on detailed analyses including sales trend and profitability trends. This allows for a method of managing distribution channels while addressing pricing imbalances.</p>

    <svg class="chart" style="left:10px;top:418px" width="340" height="170" viewBox="0 0 340 170">
      <text class="title" x="185" y="18" text-anchor="middle">Portfolio Exposure</text>
      <g stroke="var(--grid)" stroke-width="0.8">
        <line x1="45" x2="325" y1="33" y2="33"/><line x1="45" x2="325" y1="44.1" y2="44.1"/>
        <line x1="45" x2="325" y1="55.2" y2="55.2"/><line x1="45" x2="325" y1="66.3" y2="66.3"/>
        <line x1="45" x2="325" y1="77.4" y2="77.4"/><line x1="45" x2="325" y1="88.5" y2="88.5"/>
        <line x1="45" x2="325" y1="99.6" y2="99.6"/><line x1="45" x2="325" y1="110.7" y2="110.7"/>
        <line x1="45" x2="325" y1="121.8" y2="121.8"/>
      </g>
      <line x1="45" x2="325" y1="133" y2="133" stroke="#888" stroke-width="0.8"/>
      <line x1="45" x2="45" y1="33" y2="133" stroke="#888" stroke-width="0.8"/>
      <g class="tick" text-anchor="end">
        <text x="41" y="35">550</text><text x="41" y="46">540</text><text x="41" y="57">530</text>
        <text x="41" y="68">520</text><text x="41" y="79">510</text><text x="41" y="90">500</text>
        <text x="41" y="101">490</text><text x="41" y="113">480</text><text x="41" y="124">470</text><text x="41" y="135">460</text>
      </g>
      <text class="axis-title" transform="translate(14,83) rotate(-90)" text-anchor="middle">Portfolio Score</text>
      <polyline fill="none" stroke="var(--bar)" stroke-width="1.4" points="45,63 54,53 63.1,55.2 72.1,61.9 81.1,60.8 90.2,44.1 99.2,46.3 108.2,54.1 117.3,54.1 126.3,43 135.3,46.3 144.4,57.4 153.4,57.4 162.4,44.1 171.5,48.6 180.5,56.3 189.5,64.1 198.5,50.8 207.6,50.8 216.6,61.9 225.6,68.6 234.7,61.9 243.7,67.4 252.7,86.3 261.8,94.1 270.8,86.3 279.8,87.4 288.9,97.4 297.9,99.7 306.9,87.4 316,91.9 325,100.8"/>
      <g class="tick" text-anchor="end">
        <text transform="translate(47,137) rotate(-90)">2001/Q1</text>
        <text transform="translate(65,137) rotate(-90)">2001/Q3</text>
        <text transform="translate(83,137) rotate(-90)">2002/Q1</text>
        <text transform="translate(101,137) rotate(-90)">2002/Q3</text>
        <text transform="translate(120,137) rotate(-90)">2003/Q1</text>
        <text transform="translate(138,137) rotate(-90)">2003/Q3</text>
        <text transform="translate(156,137) rotate(-90)">2004/Q1</text>
        <text transform="translate(174,137) rotate(-90)">2004/Q3</text>
        <text transform="translate(192,137) rotate(-90)">2005/Q1</text>
        <text transform="translate(210,137) rotate(-90)">2005/Q3</text>
        <text transform="translate(228,137) rotate(-90)">2006/Q1</text>
        <text transform="translate(246,137) rotate(-90)">2006/Q3</text>
        <text transform="translate(264,137) rotate(-90)">2007/Q1</text>
        <text transform="translate(282,137) rotate(-90)">2007/Q3</text>
        <text transform="translate(300,137) rotate(-90)">2008/Q1</text>
        <text transform="translate(318,137) rotate(-90)">2008/Q3</text>
      </g>
    </svg>

    <svg class="chart" style="left:390px;top:418px" width="290" height="200" viewBox="0 0 290 200">
      <text class="title" x="155" y="18" text-anchor="middle">Premium Change</text>
      <g stroke="var(--grid)" stroke-width="0.8">
        <line x1="45" x2="275" y1="30" y2="30"/><line x1="45" x2="275" y1="50" y2="50"/>
        <line x1="45" x2="275" y1="70" y2="70"/><line x1="45" x2="275" y1="110" y2="110"/>
        <line x1="45" x2="275" y1="130" y2="130"/><line x1="45" x2="275" y1="150" y2="150"/>
        <line x1="45" x2="275" y1="170" y2="170"/>
      </g>
      <line x1="45" x2="275" y1="90" y2="90" stroke="#888" stroke-width="0.8"/>
      <line x1="45" x2="45" y1="30" y2="170" stroke="#888" stroke-width="0.8"/>
      <g class="tick" text-anchor="end">
        <text x="41" y="32">60%</text><text x="41" y="52">40%</text><text x="41" y="72">20%</text>
        <text x="41" y="92">0%</text><text x="41" y="112">-20%</text><text x="41" y="132">-40%</text>
        <text x="41" y="152">-60%</text><text x="41" y="172">-80%</text>
      </g>
      <g fill="var(--bar)">
        <rect x="59" y="90" width="26" height="7"/>
        <rect x="116.5" y="90" width="26" height="60"/>
        <rect x="174" y="41" width="26" height="49"/>
        <rect x="231.5" y="65" width="26" height="25"/>
      </g>
      <g class="tick" text-anchor="middle">
        <text x="72" y="99">1</text><text x="129.5" y="99">2</text>
        <text x="187" y="99">3</text><text x="244.5" y="99">4</text>
      </g>
      <text class="axis-title" x="160" y="180" text-anchor="middle">Segment Number</text>
      <text class="axis-title" transform="translate(14,100) rotate(-90)" text-anchor="middle">% Change</text>
    </svg>
  </section>

  <p class="closing">Through the use of these advanced analytics your company has the<br>opportunity to future proof each of your portfolios.</p>

  <p class="about">Brightfen Metrics provides breakthrough predictive analytics powered by machine learning and the latest statistical techniques, enabling property and casualty insurers to achieve superior performance.</p>

  <div class="footer-rule"></div>
  <p class="footer">
    <span class="company">Brightfen Metrics</span>
    218 Harlow Avenue, Suite 400, Dunmore, NC 27310, Phone: 555.214.3390, Fax: 555.214.3391<br>
    www.brightfenmetrics.com
  </p>
</div>
</body>
</html>
```